Global Careers Business Needs a Flyer Design

We need a flyer design to promote our Open Road Days seminars.
We provide free career tools and insights to young professionals through our business Fresh Pathfinders.

We would like to see our corporate colours utilised in the flyer
Grey R66 G73 B74
Teal R38 G128 B138
White R242 G240 B230

Attached is the flyer content, logo of our business and the image we wish to be used. Please note we would like to see two options of the image reflected in our teal corporate colour and a black and white option.

The final design should communicate a professional, eye-catching finish with a layout that captures the attention of our online users. Open to portrait or landscape layout.
Updates

Please note I will also require a JPEG file as well as the PDF for this piece of work. Added Friday, June 26, 2015

Target Market(s)

20-30's

Industry/Entity Type

Business

Font styles to use
Serif
Sans Serif
Other font styles liked:
• Calibri, Helvetica

Requirements
Must have
• Logo
• a DESIGN element -I do not wish to see the content just pasted onto the image. Please consider a design element, font styles, colours, etc
Nice to have
• Consider highlighting the quote by Mina Dellaway.
Should not have
• I do not wish to see the content just pasted onto the image. Please consider a design element, font styles, colours, etc

```html
<!DOCTYPE html>
<html lang="en">
<head>
<meta charset="utf-8">
<title>Open Road Days – Seminar Flyer</title>
<link rel="stylesheet" href="https://fonts.googleapis.com/css2?family=Cormorant+Garamond:wght@500&family=Oswald:wght@300;500&family=Roboto:wght@300;400;500&display=swap">
<style>
  :root {
    --grey: #42494a;
    --grey-soft: #5f6566;
    --teal: #26808a;
    --sky-light: #e4f1f2;
    --sky-mid: #b9dcdf;
    --sky-deep: #86c2c8;
    --paper: #ffffff;
    --backdrop: #e9e9e7;
  }
  * { margin: 0; padding: 0; box-sizing: border-box; }
  html, body { width: 1200px; height: 1200px; overflow: hidden; background: var(--backdrop); }
  body { font-family: "Roboto", Helvetica, Arial, sans-serif; color: var(--grey); }

  .flyer {
    position: absolute; left: 146px; top: 31px;
    width: 909px; height: 1138px;
    background: var(--paper);
    overflow: hidden;
  }

  .hero-image {
    position: absolute; left: 0; top: 250px;
    width: 100%; height: 618px;
    background:
      radial-gradient(ellipse at 20% 30%, rgba(255,255,255,0.9) 0%, rgba(255,255,255,0) 55%),
      linear-gradient(180deg, var(--paper) 0%, var(--sky-light) 22%, var(--sky-mid) 65%, var(--sky-deep) 100%);
  }

  .title {
    position: absolute; left: 40px; top: 44px; width: 829px;
    font-family: "Cormorant Garamond", Georgia, serif;
    font-weight: 500; font-size: 90px; line-height: 1;
    letter-spacing: 0; color: var(--grey); white-space: nowrap;
  }
  .title .accent { color: var(--teal); }

  .intro {
    position: absolute; left: 40px; top: 166px; width: 830px;
    font-size: 16.5px; line-height: 1.3; font-weight: 300; color: var(--grey-soft);
  }
  .intro p + p { margin-top: 11px; }

  .quote-block {
    position: absolute; left: 40px; top: 462px; width: 510px;
    border-left: 3px solid var(--paper);
    padding-left: 18px; padding-top: 4px;
  }
  .speaker {
    font-size: 22px; line-height: 1.3; font-weight: 300; color: var(--grey);
  }
  .speaker strong { font-weight: 500; }
  .quote {
    margin-top: 14px;
    font-family: "Oswald", "Arial Narrow", sans-serif; font-weight: 300;
    font-size: 28px; line-height: 1.55; color: var(--grey);
  }
  .quote .mark {
    color: var(--teal); font-weight: 500; font-size: 72px; line-height: 0;
    position: relative; top: 24px;
  }

  .teal-rule {
    position: absolute; left: 0; top: 868px; width: 100%; height: 5px;
    background: var(--teal);
  }

  .outline {
    position: absolute; left: 40px; top: 912px; width: 420px;
  }
  .outline h2 {
    font-size: 23px; font-weight: 300; color: var(--grey); margin-bottom: 12px;
  }
  .outline ul { list-style: none; }
  .outline li {
    font-size: 16.5px; font-weight: 300; line-height: 21.5px; color: var(--grey-soft);
  }
  .outline li::before { content: "▪ "; font-size: 12px; }
  .outline .audience {
    margin-top: 20px; font-size: 16.5px; font-weight: 300; line-height: 21.5px; color: var(--grey-soft);
  }

  .brand {
    position: absolute; left: 500px; top: 1000px;
    display: flex; align-items: center; gap: 22px;
  }
  .brand-dot {
    width: 52px; height: 52px; border-radius: 50%;
    border: 3px solid var(--teal); flex: none;
  }
  .brand-name {
    font-family: "Roboto", Helvetica, Arial, sans-serif;
    font-weight: 500; font-size: 36px; line-height: 1.1;
    letter-spacing: 3px; color: var(--teal); text-transform: uppercase;
  }
</style>
</head>
<body>
  <main class="flyer">
    <div class="hero-image" role="img" aria-label="Photograph of a rollercoaster track climbing against a pale teal sky"></div>

    <h1 class="title"><span class="accent">OPEN ROAD</span> DAYS</h1>

    <section class="intro">
      <p>Making the transition from school or university to work is no small step. In fact studies show that young people require considerable support during this early stage to ensure their employment is sustained.</p>
      <p>With the average person spending over 90,000 hours of their life at work, and changing jobs seven to eight times before thirty - It's critical to prepare.</p>
      <p>Open Road Days is a high energy seminar that addresses key elements, often lost and forgotten in the lead up to entering the workforce.</p>
    </section>

    <blockquote class="quote-block">
      <p class="speaker"><strong>Mina Dellaway,</strong> a passionate and outspoken former career banker turned entrepreneur delivers a message with conviction.</p>
      <p class="quote"><span class="mark">“</span> Young people need to view their career as the equivalent of a rollercoaster ride but believe they can control the dips and turns.<span class="mark">”</span></p>
    </blockquote>

    <div class="teal-rule"></div>

    <section class="outline">
      <h2>Open Road Days will explore how to:</h2>
      <ul>
        <li>Overcome setbacks at work</li>
        <li>Influence what people say about you</li>
        <li>Embrace both good and not so good feedback</li>
        <li>Start building a success story for your future</li>
      </ul>
      <p class="audience">This seminar is ideal for high school leavers, college graduates and developing young professionals.</p>
    </section>

    <div class="brand">
      <span class="brand-dot"></span>
      <span class="brand-name">Fresh<br>Pathfinders</span>
    </div>
  </main>
</body>
</html>
```